Harbor's Hymn Single Cover for iTunes etc

I am releasing a single out and I would like a simple cover design. This single cover will only be used online I.e. iTunes Spotify . I am going for a simple hipster rustic look. I have attached my photo that should be included in the design. If possible I would rather the photo just edited and words added . Thank you

Target Market(s)

Teens to 40s contempary Christians

Industry/Entity Type

Music Download

Requirements
Must have
• -The picture below
• -Marisol Penrow
• -Harbor's hymn

```html
<!DOCTYPE html>
<html lang="en">
<head>
<meta charset="utf-8">
<title>Harbor's Hymn – Single Cover</title>
<link href="https://fonts.googleapis.com/css2?family=Josefin+Sans:wght@100;300&display=swap" rel="stylesheet">
<style>
  :root {
    --stage: #d4d4d4;
    --title-gold: #f1c542;
    --artist-white: #f6f1ea;
    --sun-peach: #eab27a;
    --ember: #c8693a;
    --dusk: #5b4841;
    --night: #211d1c;
    --portrait-warm: #7a3f24;
    --portrait-deep: #1a1412;
  }
  html, body {
    margin: 0;
    width: 1190px;
    height: 1200px;
    overflow: hidden;
    background: var(--stage);
  }
  .single-cover {
    position: absolute;
    left: 45px;
    top: 50px;
    width: 1100px;
    height: 1100px;
    display: block;
  }
  .cover-title {
    font-family: "Josefin Sans", sans-serif;
    font-weight: 100;
    fill: var(--title-gold);
  }
  .cover-artist {
    font-family: "Josefin Sans", sans-serif;
    font-weight: 300;
    fill: var(--artist-white);
    font-size: 32px;
  }
</style>
</head>
<body>
<svg class="single-cover" viewBox="0 0 1100 1100" xmlns="http://www.w3.org/2000/svg">
  <defs>
    <linearGradient id="warm-fade" x1="0" y1="0" x2="0" y2="1">
      <stop offset="0" stop-color="var(--sun-peach)"/>
      <stop offset="0.35" stop-color="var(--ember)"/>
      <stop offset="0.7" stop-color="var(--dusk)"/>
      <stop offset="1" stop-color="var(--night)"/>
    </linearGradient>
    <linearGradient id="portrait-fill" x1="0" y1="0" x2="0" y2="1">
      <stop offset="0" stop-color="var(--portrait-warm)"/>
      <stop offset="0.45" stop-color="#4a2a1e"/>
      <stop offset="1" stop-color="var(--portrait-deep)"/>
    </linearGradient>
  </defs>

  <g class="cover-background" role="img" aria-label="Outdoor scene with bare trees and a road in warm golden sunset haze">
    <rect width="1100" height="1100" fill="url(#warm-fade)"/>
  </g>

  <g class="artist-portrait" role="img" aria-label="Photo of the singer seated cross-legged, smiling, lit by warm sunset light">
    <rect x="500" y="40" width="600" height="1060" rx="260" ry="260" fill="url(#portrait-fill)" opacity="0.9"/>
    <rect x="500" y="600" width="600" height="500" fill="var(--portrait-deep)" opacity="0.85"/>
  </g>

  <g class="light-facets" fill="#ffffff">
    <polygon points="0,640 1100,260 1100,420 0,820" opacity="0.06"/>
    <polygon points="600,0 1100,0 1100,300" opacity="0.07"/>
    <polygon points="0,880 700,1100 0,1100" opacity="0.05"/>
  </g>

  <text class="cover-title" x="29" y="547" font-size="210" textLength="1002" lengthAdjust="spacingAndGlyphs">HARBOR'S</text>
  <text class="cover-title" x="63" y="826" font-size="365" textLength="1003" lengthAdjust="spacingAndGlyphs">HYMN</text>

  <text class="cover-artist" x="35" y="1028" textLength="1031" lengthAdjust="spacing">MARISOL PENROW</text>
</svg>
</body>
</html>
```